Presentation Folder for Brisk Estates

We are a new property management / real estate company in Denver Colorado and are in need of new stationary design. Attached are our business card and logo deigns. We are looking for our stationary design. We need a presentation folder design that is Professional, exciting, and approachable. We do not have a preference on folder layout (pockets, style of folding) but will most likely be using a standard two pocket folder design (roughly 9x12) but feel free to experiment with and folder style as long as we can find a place to print them. We would also like to have a matching letterhead/page design
Below is standard size of folder from lumo press
Full Bleed Size
20.87" x 16.68"
53 x 42.4 cm
6260 x 5004 pixels
Document Trim Size
20.75" x 16.56"
52.7 x 42.1 cm
6225 x 4969 pixels
Target Market(s)
We are attempting to target the top end of the real estate market in Denver Colorado. Are target market is investors in real estate.
Industry/Entity Type
Property Management
Font styles to use
Other font styles liked:
- Would like to keep font same to logo
Look and feel
Each slider illustrates characteristics of the customer's brand and the style your logo design should communicate.

```html
<!DOCTYPE html>
<html lang="en">
<head>
<meta charset="utf-8">
<title>Brisk Estates – Presentation Folder</title>
<link rel="stylesheet" href="https://fonts.googleapis.com/css2?family=Oswald:wght@500&family=Open+Sans:wght@400&display=swap">
<style>
  :root {
    --backdrop: #0d3a48;
    --paper: #ffffff;
    --paper-shade: #e9e9ea;
    --panel-grey: #616161;
    --panel-grey-dark: #4d4d4d;
    --brand-blue: #5aa6c6;
    --brand-grey: #6d6d6d;
    --faint-mark: #d8dde1;
  }
  * { margin: 0; padding: 0; box-sizing: border-box; }
  html, body { width: 1200px; height: 802px; overflow: hidden; }
  body { background: var(--backdrop); position: relative; font-family: "Oswald", sans-serif; }

  .folder-cover {
    position: absolute; left: 50px; top: 140px; width: 340px; height: 520px;
    background: linear-gradient(160deg, var(--paper) 60%, var(--paper-shade));
    display: flex; flex-direction: column; align-items: center; justify-content: center;
  }
  .cover-name { font-size: 34px; font-weight: 500; color: var(--brand-blue); letter-spacing: 1px; }
  .cover-tagline { font-family: "Open Sans", sans-serif; font-size: 10px; color: var(--brand-grey); letter-spacing: 2px; text-transform: uppercase; margin-top: 2px; }

  .folder-spread { position: absolute; left: 420px; top: 110px; width: 740px; height: 560px; display: flex; }
  .folder-panel { position: relative; width: 370px; height: 560px; overflow: hidden; }
  .panel-left { background: linear-gradient(150deg, var(--paper) 40%, var(--paper-shade)); }
  .panel-right { background: linear-gradient(150deg, var(--panel-grey) 30%, var(--panel-grey-dark)); }

  .faint-name {
    position: absolute; left: 0; right: 0; top: 190px; text-align: center;
    font-size: 44px; font-weight: 500; color: var(--faint-mark); letter-spacing: 1px;
  }

  .pocket { position: absolute; left: 0; bottom: 0; width: 370px; height: 150px; }
  .pocket svg { position: absolute; inset: 0; }
  .pocket-name {
    position: absolute; top: 58px; font-size: 22px; font-weight: 500; color: var(--brand-blue); letter-spacing: 0.5px;
  }
  .pocket-left .pocket-name { left: 95px; }
  .pocket-right .pocket-name { left: 165px; }
</style>
</head>
<body>
  <section class="folder-cover">
    <p class="cover-name">Brisk Estates</p>
    <p class="cover-tagline">Property Management</p>
  </section>

  <section class="folder-spread">
    <div class="folder-panel panel-left">
      <p class="faint-name">Brisk Estates</p>
      <div class="pocket pocket-left">
        <svg width="370" height="150" viewBox="0 0 370 150">
          <defs>
            <linearGradient id="pocketFillLeft" x1="0" y1="0" x2="1" y2="1">
              <stop offset="0" stop-color="#ffffff"/>
              <stop offset="1" stop-color="#e4e4e4"/>
            </linearGradient>
          </defs>
          <path d="M0 0 H260 C300 0 315 20 330 50 L370 150 H0 Z" fill="url(#pocketFillLeft)"/>
        </svg>
        <p class="pocket-name">Brisk Estates</p>
      </div>
    </div>
    <div class="folder-panel panel-right">
      <div class="pocket pocket-right">
        <svg width="370" height="150" viewBox="0 0 370 150">
          <defs>
            <linearGradient id="pocketFillRight" x1="0" y1="0" x2="1" y2="1">
              <stop offset="0" stop-color="#ffffff"/>
              <stop offset="1" stop-color="#e6e6e6"/>
            </linearGradient>
          </defs>
          <path d="M370 0 H110 C70 0 55 20 40 50 L0 150 H370 Z" fill="url(#pocketFillRight)"/>
        </svg>
        <p class="pocket-name">Brisk Estates</p>
      </div>
    </div>
  </section>
</body>
</html>
```